Demolition Company Billboard Design 13 feet wide 15 feet high

This is my first billboard on a busy road. I want it to be professional but with some eye catching flair that matches by business which is a demoltion business and also list my services. My company slogan is also

"call hollick, watch it fall"

Target Market(s)

Home Ownerd and General Construction Companies

Industry/Entity Type

construction

Colors
0054AA
0677BA
7BADD7
CADEEF
E8F1F8

Requirements
Must have
• My services listed in the pictures my website and my phone number

```html
<!DOCTYPE html>
<html lang="en">
<head>
<meta charset="utf-8">
<title>Dale Hollick Demolition Billboard</title>
<link rel="stylesheet" href="https://fonts.googleapis.com/css2?family=Anton&family=Montserrat:wght@500;600;700;800&display=swap">
<style>
  :root {
    --page-bg: #dcdcdc;
    --photo-top: #6b6e70;
    --photo-mid: #3e3029;
    --photo-low: #221c19;
    --brand-blue: #0677BA;
    --brand-blue-dark: #0054AA;
    --accent-orange: #f47b20;
    --white: #ffffff;
    --footer-dark: #181818;
  }
  * { margin: 0; padding: 0; box-sizing: border-box; }
  html, body {
    width: 1200px; height: 2204px; overflow: hidden;
    background: radial-gradient(ellipse at center, #f2f2f2 0%, var(--page-bg) 75%);
    font-family: "Montserrat", sans-serif;
  }
  .billboard {
    position: absolute; left: 40px; top: 457px;
    width: 1120px; height: 1290px; overflow: hidden;
    box-shadow: 0 30px 50px rgba(0,0,0,0.25);
  }
  .billboard__photo {
    position: absolute; left: 0; top: 0; width: 1120px; height: 1171px;
    background: linear-gradient(180deg, var(--photo-top) 0%, #5a524c 15%, var(--photo-mid) 40%, #3a2c24 70%, var(--photo-low) 100%);
  }
  .billboard__photo::after {
    content: ""; position: absolute; right: 60px; top: 260px; width: 560px; height: 780px;
    background: radial-gradient(ellipse at 55% 50%, rgba(214,128,40,0.55) 0%, rgba(214,128,40,0.15) 45%, transparent 70%);
  }
  .brand {
    position: absolute; left: 80px; top: 52px;
    display: flex; align-items: center; gap: 22px;
  }
  .brand__square { width: 60px; height: 60px; background: var(--white); }
  .brand__name {
    color: var(--white); font-weight: 700; font-size: 40px; line-height: 40px;
    text-transform: uppercase; letter-spacing: 1px;
  }
  .headline {
    position: absolute; left: 82px; top: 268px;
    font-family: "Anton", sans-serif; color: var(--white);
    font-size: 126px; line-height: 132px; text-transform: uppercase;
    letter-spacing: 2px; text-shadow: 0 4px 10px rgba(0,0,0,0.5);
  }
  .scope-list {
    position: absolute; left: 94px; top: 696px; list-style: none;
    color: var(--white); font-size: 29px; font-weight: 500; line-height: 41px;
  }
  .scope-list li { display: flex; align-items: center; gap: 18px; }
  .scope-list li::before { content: ""; width: 13px; height: 13px; background: var(--brand-blue); }
  .services {
    position: absolute; left: 0; top: 987px; width: 1120px; height: 184px;
    background: var(--brand-blue);
  }
  .services__badge {
    position: absolute; left: 384px; top: 958px; width: 351px; height: 58px;
    background: var(--accent-orange); border-radius: 8px;
    color: var(--white); font-weight: 800; font-size: 40px; line-height: 58px;
    text-align: center; letter-spacing: 0.5px;
  }
  .services__grid {
    position: absolute; left: 80px; top: 1040px;
    display: grid; grid-template-columns: 322px 392px 300px; row-gap: 18px;
    list-style: none;
  }
  .services__grid li {
    display: flex; align-items: center; gap: 14px;
    color: var(--white); font-weight: 800; font-size: 33px; line-height: 42px;
  }
  .services__grid li::before {
    content: ""; width: 12px; height: 12px; border: 2px solid var(--white); opacity: 0.85;
  }
  .contact {
    position: absolute; left: 0; top: 1171px; width: 1120px; height: 119px;
    background: linear-gradient(180deg, #232323, var(--footer-dark));
    display: flex; align-items: center; color: var(--white);
  }
  .contact__phone {
    position: absolute; left: 72px; display: flex; align-items: center; gap: 12px;
    font-weight: 700; font-size: 50px;
  }
  .contact__web {
    position: absolute; left: 560px; display: flex; align-items: center; gap: 14px;
    font-weight: 600; font-size: 35px;
  }
</style>
</head>
<body>
  <main class="billboard">
    <div class="billboard__photo" role="img" aria-label="Photo of an orange tracked excavator demolishing an old brick building under a grey sky, rubble in the foreground"></div>

    <div class="brand">
      <span class="brand__square"></span>
      <span class="brand__name">Dale Hollick<br>Demolition, LLC</span>
    </div>

    <h1 class="headline">Call Hollick,<br>Watch It<br>Fall</h1>

    <ul class="scope-list">
      <li>INTERIOR</li>
      <li>COMMERCIAL</li>
      <li>EXTERIOR</li>
    </ul>

    <section class="services"></section>
    <div class="services__badge">OUR SERVICES</div>
    <ul class="services__grid">
      <li>Room Gut Out</li>
      <li>Partial Demolition</li>
      <li>Commercial</li>
      <li>House Gut Out</li>
      <li>Full Demolition</li>
      <li>Residential</li>
    </ul>

    <footer class="contact">
      <div class="contact__phone">
        <svg width="46" height="46" viewBox="0 0 24 24" aria-hidden="true">
          <path fill="#fff" d="M6.6 10.8a15.1 15.1 0 0 0 6.6 6.6l2.2-2.2c.3-.3.7-.4 1-.2 1.1.4 2.3.6 3.6.6.6 0 1 .4 1 1V20c0 .6-.4 1-1 1A17 17 0 0 1 3 4c0-.6.4-1 1-1h3.5c.6 0 1 .4 1 1 0 1.3.2 2.5.6 3.6.1.3 0 .7-.2 1z"/>
          <path fill="none" stroke="#fff" stroke-width="1.6" d="M14.5 3.5a6.5 6.5 0 0 1 6 6M14 6.8a3.4 3.4 0 0 1 3.2 3.2"/>
        </svg>
        (412) 555-0148
      </div>
      <div class="contact__web">
        <svg width="32" height="32" viewBox="0 0 24 24" aria-hidden="true" fill="none" stroke="#fff" stroke-width="1.8">
          <circle cx="12" cy="12" r="10"/>
          <ellipse cx="12" cy="12" rx="4.5" ry="10"/>
          <path d="M2 12h20M4 7h16M4 17h16"/>
        </svg>
        www.hollickwrecking.com
      </div>
    </footer>
  </main>
</body>
</html>
```